HearthBond USA needs a Prayer booklet

I need a bookmark 2.5 x 8.5, full color, 2-sided, that lists a number of questions for married couples to ask themselves. The numbering is a little mixed up. Please make it look good.
My layout started with a different idea, but now would like it to be the shape of a larger bookmark.

Target Market(s)

Church

```html
<!DOCTYPE html>
<html lang="en">
<head>
<meta charset="utf-8">
<title>An Examination Of Conscience For The Married – HearthBond USA</title>
<link rel="stylesheet" href="https://fonts.googleapis.com/css2?family=Lobster&family=Ubuntu:ital,wght@0,400;1,400&family=Noto+Serif:wght@700&family=Hind:wght@400&display=swap">
<style>
  :root {
    --stage: #efeadd;
    --copper: #c27a3c;
    --copper-dark: #a8682f;
    --blush: #e7b9b3;
    --cream: #fbf5ec;
    --sand: #f0d2a6;
    --ink: #2b2622;
    --prose: #4a433e;
    --navy: #1d4f72;
  }
  * { box-sizing: border-box; margin: 0; padding: 0; }
  html, body { width: 1200px; height: 1200px; overflow: hidden; }
  body { background: var(--stage); position: relative; font-family: "Hind", sans-serif; }

  .card { position: absolute; overflow: hidden; box-shadow: 0 4px 14px rgba(0,0,0,.18); }

  /* Front cover */
  .front { left: 40px; top: 40px; width: 560px; height: 430px; background: var(--cream); }
  .front .photo { position: absolute; inset: 0 0 110px 0;
    background: radial-gradient(ellipse at 60% 40%, #f3e2cf 0%, #d9b795 45%, #8b6a4f 80%, #6e5440 100%); }
  .front svg.swoops { position: absolute; inset: 0; }
  .front .title { position: absolute; left: 0; right: 0; bottom: 22px; text-align: center;
    font-family: "Lobster", cursive; color: var(--copper); font-size: 40px; font-weight: 400; line-height: 1.15;
    transform: rotate(-3deg); }

  /* Back cover */
  .back { left: 620px; top: 40px; width: 540px; height: 430px; background: var(--cream); }
  .back .photo { position: absolute; inset: 0;
    background: linear-gradient(160deg, #d8c9b0 0%, #c9b89c 40%, #e8cfc3 75%, #f5e9de 100%); opacity: .9; }
  .back .prayer { position: absolute; left: 26px; top: 22px; right: 24px; }
  .back .prayer h2 { font-family: "Lobster", cursive; color: var(--copper); font-size: 32px; font-weight: 400; }
  .back .prayer p { font-family: "Ubuntu", sans-serif; font-style: italic; color: var(--prose);
    font-size: 15.5px; line-height: 1.45; margin-top: 6px; }
  .back .org { position: absolute; left: 0; right: 0; top: 250px; text-align: center;
    font-family: "Ubuntu", sans-serif; font-weight: 400; color: var(--navy); font-size: 24px; }
  .back .org .dot { display: inline-block; width: 14px; height: 14px; border-radius: 50%;
    background: var(--navy); margin-right: 10px; vertical-align: 1px; }
  .back .order { position: absolute; left: 0; right: 0; bottom: 34px; text-align: center;
    font-family: "Noto Serif", serif; font-weight: 700; color: var(--ink); font-size: 14.5px; line-height: 1.4; }
  .back .order .icon { display: inline-block; vertical-align: -3px; margin: 0 3px; }
  .rule { position: absolute; left: 50%; width: 180px; height: 1px; background: #9a8c80; transform: translateX(-50%); }
  .back .rule { bottom: 20px; }

  /* Inside spread */
  .inside { left: 40px; top: 510px; width: 1120px; height: 650px; background: #f6ebe0; }
  .inside .photo { position: absolute; left: 0; top: 0; width: 560px; height: 100%;
    background: radial-gradient(ellipse at 50% 65%, #e2cfc1 0%, #efe2d6 45%, #f6ebe0 80%); }
  .inside svg.swoops { position: absolute; inset: 0; }
  .inside .fold { position: absolute; left: 560px; top: 0; bottom: 0; border-left: 1px dashed #c9b8a8; }
  .page { position: absolute; top: 0; bottom: 0; width: 560px; }
  .page.left { left: 0; } .page.right { left: 561px; }
  .page .stripe { position: absolute; left: 0; top: 0; bottom: 0; width: 34px; background: var(--sand); }
  .questions { position: absolute; left: 12px; right: 22px; top: 16px; list-style: none;
    color: var(--prose); font-size: 15.5px; line-height: 1.3; }
  .questions li { display: flex; margin-bottom: 4px; }
  .questions .n { width: 30px; flex: none; }
  .questions .blank { flex: 1; height: 22px; background: #fff; }
  .page .rule { bottom: 28px; }
</style>
</head>
<body>

<section class="card front">
  <div class="photo" role="img" aria-label="Sepia photo of a couple seen from behind on a bench before a manor house and garden"></div>
  <svg class="swoops" width="560" height="430" viewBox="0 0 560 430" aria-hidden="true">
    <path d="M0 0 H560 V20 C380 20 170 90 0 300 Z" fill="#f6e7d6" opacity=".75"/>
    <path d="M0 330 C140 150 340 40 560 20 V60 C350 90 170 190 40 330 Z" fill="var(--blush)" opacity=".55"/>
    <path d="M0 320 Q280 260 560 285 V430 H0 Z" fill="var(--cream)" opacity=".88"/>
    <path d="M0 320 Q280 262 560 285" fill="none" stroke="var(--copper-dark)" stroke-width="7"/>
  </svg>
  <h1 class="title">An Examination Of Conscience<br>For The Married</h1>
</section>

<section class="card back">
  <div class="photo" role="img" aria-label="Soft faded garden photo with trees and flower beds"></div>
  <div class="prayer">
    <h2>Act of Contrition</h2>
    <p>O my God, I am heartily sorry for having offended you. I detest all my sins because of your just punishment, but most of all because they offend you, my God, who art all-good and deserving of all my love. I firmly resolve, with the help of your grace, to sin no more, and to avoid the near occasion of sin. Amen.</p>
  </div>
  <p class="org"><span class="dot"></span>HearthBond USA</p>
  <p class="order">Additional quantity copies of<br>
    AN EXAMINATION OF CONSCIENCE FOR THE MARRIED are available<br>
    from <svg class="icon" width="16" height="16" viewBox="0 0 16 16" aria-hidden="true"><circle cx="8" cy="8" r="7" fill="var(--navy)"/><path d="M1 8h14M8 1c-3 4-3 10 0 14M8 1c3 4 3 10 0 14" stroke="#fff" stroke-width="1" fill="none"/></svg>www.hearthbondusa.org<br>
    or by contacting Tom &amp; Ellen Marsh at <svg class="icon" width="16" height="16" viewBox="0 0 16 16" aria-hidden="true"><rect width="16" height="16" rx="3" fill="var(--navy)"/><path d="M5 3l2 3-1 1.5c.8 1.5 1.8 2.5 3.5 3.5L11 10l3 2-1.5 2C8 14 3 9 3 4.5Z" fill="#fff"/></svg>(555) 014-0199.</p>
  <div class="rule"></div>
</section>

<section class="card inside">
  <div class="photo" role="img" aria-label="Faint close-up photo of two joined hands with wedding rings"></div>
  <svg class="swoops" width="1120" height="650" viewBox="0 0 1120 650" aria-hidden="true">
    <path d="M600 650 C760 520 920 460 1120 430 V480 C930 510 780 570 690 650 Z" fill="var(--blush)" opacity=".55"/>
    <path d="M980 0 C1080 120 1110 300 1060 650 H1120 V0 Z" fill="#fbf2e8" opacity=".8"/>
  </svg>
  <div class="fold"></div>

  <div class="page left">
    <div class="stripe"></div>
    <ol class="questions">
      <li><span class="n">1.</span><span>Have I said thoughtless or hurtful words, yelled indiscriminately, or in any other way been unkind or uncharitable to my spouse or family members?</span></li>
      <li><span class="n">2.</span><span>Have I been angry at my spouse?</span></li>
      <li><span class="n">3.</span><span>Have I allowed resentments and bitterness toward my spouse to take root in my mind?</span></li>
      <li><span class="n">4.</span><span>Has pride or selfishness caused me to stumble and fall short in my marriage?</span></li>
      <li><span class="n">5.</span><span>Do I have an attitude that I’m right and my spouse is always wrong?</span></li>
      <li><span class="n">6.</span><span>Have I been hard-hearted or callous?</span></li>
      <li><span class="n">7.</span><span>Have I been unfair, causing pain, resentment and hurt in my marriage?</span></li>
      <li><span class="n">8.</span><span>Are my priorities misplaced?</span></li>
      <li><span class="n">9.</span><span>Am I defensive or critical of my spouse, of my children?</span></li>
      <li><span class="n">10.</span><span>Have I been rude or self-seeking?</span></li>
      <li><span class="n">11.</span><span>Do I keep a record of wrongs?</span></li>
      <li><span class="n">12.</span><span>Have I been unsupportive?</span></li>
      <li><span class="n">13.</span><span>Have I spoken sharply or sarcastically to my spouse? Have I spoken in a demeaning or negative way?</span></li>
    </ol>
    <div class="rule"></div>
  </div>

  <div class="page right">
    <div class="stripe"></div>
    <ol class="questions">
      <li><span class="n">14.</span><span>Have I failed to seek God’s plan for our marriage?</span></li>
      <li><span class="n">15.</span><span>Has infidelity, pornography, overspending occurred?</span></li>
      <li><span class="n">16.</span><span>Have I failed to follow the teachings of the Church on Family Planning?</span></li>
      <li><span class="n">17.</span><span>Have I failed to turn to God in prayer?</span></li>
      <li><span class="n">18.</span><span>Have I been unwilling to work to make our marriage healthy?</span></li>
      <li><span class="n">19.</span><span>Have I failed to protect my spouse?</span></li>
      <li><span class="n">20.</span><span>Have I been unwilling to make changes in my behavior? In my attitude? If so, what has been the consequences?</span></li>
      <li><span class="n">21.</span><span>Have I threatened to leave? Or avoided the problems I create?</span></li>
      <li><span class="n">22.</span><span>Have I told little lies, or big ones? Been imprecise in my words?</span></li>
      <li><span class="n">23.</span><span>Am I impatient with the ones I love?</span></li>
      <li><span class="n">24.</span><span>Have I physically abused my spouse?</span></li>
      <li><span class="n">25.</span><span>Have I gossiped about my spouse?</span></li>
      <li><span class="n">26.</span><span>Have I failed to seek forgiveness?</span></li>
      <li><span class="n">27.</span><span>Have I been unforgiving?</span></li>
      <li><span class="n">28.</span><span class="blank"></span></li>
    </ol>
    <div class="rule"></div>
  </div>
</section>

</body>
</html>
```